Voltara Solutions Ltd - Project for new electric vehicle charging company

Please use Voltara Solutions Ltd logo & artwork instead of Brightwell.

We would like to produce a leaflet to advertise our electric vehicle charging company to build a reputation and workflow in the local area.

We would like to use the attached logo and maintain the colour palette of the of the logo to be simple, modern and effective.

I have over 15 years experience in the electrical industry and have direct access to the latest technology in electric vehicle charging.

All quotes to remain fixed costs subject to survey of the property and maintenance options can be available.

We can also offer further remedial works to any property through our sister company Brightwell Solutions Ltd.

Target Market(s)

Domestic / commercial customers

Requirements
Must have
• Voltara Solutions Ltd logo and colour palette.
Should not have
• Brightwell logo, Email or website address.

```html
<!DOCTYPE html>
<html lang="en">
<head>
<meta charset="utf-8">
<title>Drive Electric. Charge With Ease. – Leaflet</title>
<link rel="stylesheet" href="https://fonts.googleapis.com/css2?family=Anton&family=Poppins:wght@400;500;600;700;800;900&display=swap">
<style>
  :root {
    --teal: #00b9a3;
    --teal-deep: #009e8b;
    --ink: #111111;
    --paper: #ffffff;
    --backdrop: #eef1f3;
    --rule: #9a9a9a;
    --illus-light: #e9efec;
    --illus-mid: #cfe3dc;
  }
  * { box-sizing: border-box; margin: 0; padding: 0; }
  html, body { width: 1200px; height: 2400px; overflow: hidden; }
  body {
    background: var(--backdrop);
    font-family: "Poppins", Arial, sans-serif;
    color: var(--ink);
    position: relative;
  }
  .leaflet {
    position: absolute;
    left: 50px; top: 423px;
    width: 1100px; height: 1553px;
    background: var(--paper);
    overflow: hidden;
    box-shadow: 0 6px 24px rgba(0,0,0,.12);
  }
  .swirls { position: absolute; inset: 0; width: 100%; height: 100%; }
  .swirls path { fill: var(--teal); }

  .headline {
    position: absolute; left: 57px; top: 70px;
    font-weight: 900; line-height: .92; letter-spacing: -1px;
  }
  .headline .line { display: block; font-size: 72px; }
  .headline .charge {
    font-family: "Anton", "Impact", sans-serif; font-weight: 400;
    color: var(--teal); font-size: 150px; line-height: 1; letter-spacing: 0;
    margin: 2px 0 -6px;
  }
  .headline .ease { font-size: 80px; }
  .divider { position: absolute; left: 57px; top: 443px; width: 363px; height: 3px; background: var(--rule); }
  .tagline {
    position: absolute; left: 57px; top: 462px;
    font-weight: 700; font-size: 33px; line-height: 1.2;
  }

  .illustration-ev {
    position: absolute; left: 250px; top: 560px; width: 800px; height: 330px;
    border-radius: 40px;
    background: radial-gradient(ellipse at 45% 55%, var(--illus-light) 0%, var(--illus-mid) 70%, rgba(207,227,220,0) 100%);
  }
  .illustration-battery {
    position: absolute; left: 648px; top: 318px; width: 266px; height: 266px;
    border-radius: 50%;
    background: radial-gradient(circle, #0d1a0d 55%, #1c3b12 80%, #56c21d 100%);
  }

  .experience { position: absolute; left: 60px; top: 905px; height: 108px; display: flex; align-items: center; }
  .experience .over {
    width: 40px; height: 108px; background: var(--teal); color: var(--paper);
    display: flex; align-items: center; justify-content: center;
    font-weight: 800; font-size: 26px;
  }
  .experience .over span { transform: rotate(-90deg); display: block; }
  .experience .number {
    font-family: "Anton", "Impact", sans-serif; color: var(--teal);
    font-size: 124px; line-height: 1; margin: 0 6px;
  }
  .experience .label { font-weight: 900; font-size: 46px; line-height: .95; letter-spacing: -2px; }
  .experience-rule { position: absolute; left: 542px; top: 905px; width: 2px; height: 100px; background: #cccccc; }
  .experience-note {
    position: absolute; left: 559px; top: 912px;
    font-size: 27px; line-height: 1.12; font-weight: 400;
  }

  .revolution-title {
    position: absolute; left: 57px; top: 1068px;
    font-weight: 900; font-size: 41px; letter-spacing: -.5px;
  }
  .revolution-title .accent { color: var(--teal); }
  .revolution-frame { position: absolute; left: 0; top: 0; width: 1100px; height: 1553px; pointer-events: none; }
  .revolution-frame path, .revolution-frame line { fill: none; stroke: var(--ink); stroke-width: 2; }
  .revolution-frame circle { fill: var(--paper); stroke: var(--ink); stroke-width: 2; }
  .revolution-frame .split { stroke: #cccccc; }
  .benefit {
    position: absolute; top: 1140px; display: flex; align-items: flex-start; gap: 23px;
    font-size: 20px; line-height: 1.2; font-weight: 500;
  }
  .benefit.fixed-costs { left: 78px; width: 450px; }
  .benefit.remedial { left: 577px; width: 460px; }
  .benefit p { white-space: nowrap; }
  .benefit .badge { flex: 0 0 60px; width: 60px; height: 60px; margin-top: 4px; }
  .benefit .badge circle.outer { fill: none; stroke: var(--teal-deep); stroke-width: 2; stroke-dasharray: 4 3; }
  .benefit .badge circle.inner { fill: none; stroke: var(--teal-deep); stroke-width: 2; }
  .benefit .badge text { fill: var(--teal-deep); font: 700 20px "Poppins", sans-serif; }

  .brand { position: absolute; left: 60px; top: 1378px; display: flex; align-items: center; gap: 18px; }
  .brand .dot { width: 84px; height: 84px; border-radius: 50%; background: var(--teal); }
  .brand .name { color: var(--teal); font-weight: 500; font-size: 62px; line-height: 1; letter-spacing: -.5px; }

  .contact { position: absolute; left: 545px; top: 1308px; }
  .contact .cta { font-weight: 900; font-size: 42px; letter-spacing: .5px; line-height: 1.1; margin-bottom: 6px; }
  .contact .cta .accent { color: var(--teal); }
  .contact ul { list-style: none; }
  .contact li { display: flex; align-items: center; gap: 14px; font-weight: 700; font-size: 30px; line-height: 1.38; }
  .contact li svg { width: 26px; height: 26px; flex: 0 0 26px; }
  .contact li svg .icon { fill: var(--teal); }
  .contact .accent { color: var(--teal); }
</style>
</head>
<body>
  <main class="leaflet">
    <svg class="swirls" viewBox="0 0 910 1285" preserveAspectRatio="none" aria-hidden="true">
      <path d="M330,0 L525,0 C540,140 510,260 440,365 C432,230 400,110 330,0 Z"/>
      <path d="M910,95 L910,300 C760,320 610,410 500,520 C380,630 200,700 0,690 L0,540 C140,565 300,545 400,470 C540,330 700,140 910,95 Z"/>
    </svg>

    <h1 class="headline">
      <span class="line">DRIVE</span>
      <span class="line">ELECTRIC.</span>
      <span class="line charge">CHARGE</span>
      <span class="line ease">WITH EASE.</span>
    </h1>
    <div class="divider"></div>
    <p class="tagline">Powering Your<br>Electric Vehicle with<br>Confidence</p>

    <div class="illustration-ev" role="img" aria-label="Illustration of a white electric van plugged into a green charging post"></div>
    <div class="illustration-battery" role="img" aria-label="Battery icon showing 72% charge inside a dark circle"></div>

    <div class="experience">
      <div class="over"><span>OVER</span></div>
      <div class="number">15</div>
      <div class="label">YEARS OF<br>EXPERIENCE</div>
    </div>
    <div class="experience-rule"></div>
    <p class="experience-note">in the electrical industry and have<br>direct access to the latest technology<br>in electric vehicle charging</p>

    <h2 class="revolution-title"><span class="accent">BE A PART OF</span> OUR REVOLUTION</h2>
    <svg class="revolution-frame" viewBox="0 0 1100 1553" aria-hidden="true">
      <path d="M57,1120 V1262 Q57,1278 73,1278 H1030 Q1046,1278 1046,1262 V1119 Q1046,1103 1030,1103 H764"/>
      <circle cx="57" cy="1116" r="4"/>
      <circle cx="760" cy="1103" r="4"/>
      <line class="split" x1="545" y1="1128" x2="545" y2="1258"/>
    </svg>
    <div class="benefit fixed-costs">
      <svg class="badge" viewBox="0 0 60 60" aria-hidden="true">
        <circle class="outer" cx="30" cy="30" r="28"/>
        <circle class="inner" cx="30" cy="30" r="18"/>
        <text x="30" y="37" text-anchor="middle">$</text>
      </svg>
      <p>All quotes to remain fixed costs<br>subject to survey of the property<br>and maintenance<br>options can be available.</p>
    </div>
    <div class="benefit remedial">
      <svg class="badge" viewBox="0 0 60 60" aria-hidden="true">
        <circle class="outer" cx="30" cy="30" r="28"/>
        <circle class="inner" cx="30" cy="30" r="18"/>
        <text x="30" y="37" text-anchor="middle">%</text>
      </svg>
      <p>We can also offer further remedial<br>works to any property through<br>our sister company Brightwell<br>Solutions Ltd.</p>
    </div>

    <div class="brand">
      <div class="dot"></div>
      <div class="name">Voltara</div>
    </div>

    <div class="contact">
      <p class="cta">CALL <span class="accent">US NOW!</span></p>
      <ul>
        <li>
          <svg viewBox="0 0 24 24" aria-hidden="true"><path class="icon" d="M6.6 10.8a15.1 15.1 0 0 0 6.6 6.6l2.2-2.2a1 1 0 0 1 1-.25 11.4 11.4 0 0 0 3.6.57 1 1 0 0 1 1 1V20a1 1 0 0 1-1 1A17 17 0 0 1 3 4a1 1 0 0 1 1-1h3.5a1 1 0 0 1 1 1c0 1.25.2 2.450.57 3.57a1 1 0 0 1-.25 1z"/></svg>
          8123 4567 8901
        </li>
        <li>
          <svg viewBox="0 0 24 24" aria-hidden="true"><path class="icon" d="M2 5h20v14H2z M4 7v.5l8 5.5 8-5.5V7z" fill-rule="evenodd"/></svg>
          info@voltarasolutions.com
        </li>
        <li>
          <svg viewBox="0 0 24 24" aria-hidden="true"><path class="icon" d="M12 2a10 10 0 1 0 0 20 10 10 0 0 0 0-20zm6.9 6h-2.9a15.7 15.7 0 0 0-1.4-3.6A8 8 0 0 1 18.9 8zM12 4c.8 1.2 1.5 2.5 1.9 4h-3.8c.4-1.5 1.1-2.8 1.9-4zM4.3 14a8 8 0 0 1 0-4h3.4a16.5 16.5 0 0 0 0 4zm.8 2h2.9c.3 1.3.8 2.5 1.4 3.6A8 8 0 0 1 5.1 16zM8 8H5.1a8 8 0 0 1 4.3-3.6C8.8 5.5 8.3 6.7 8 8zm4 12c-.8-1.2-1.5-2.5-1.9-4h3.8c-.4 1.5-1.100 2.8-1.9 4zm2.3-6H9.7a14.7 14.7 0 0 1 0-4h4.6a14.7 14.7 0 0 1 0 4zm.3 5.6c.6-1.1 1.1-2.3 1.4-3.6h2.9a8 8 0 0 1-4.3 3.6zm1.7-5.6a16.5 16.5 0 0 0 0-4h3.4a8 8 0 0 1 0 4z"/></svg>
          <span>www.<span class="accent">voltarasolutions</span>.com</span>
        </li>
      </ul>
    </div>
  </main>
</body>
</html>
```